ourAMBERstash - postcard 4.75 x 9.5

We would like a postcard 4.75" tall x 9.5" wide for our product called ourAMBERstash (oAs). Please see www.ourAMBERstash.com

There are 2 prizes:
$200 for 1st place
$100 for 2nd place.

SIDE 1
Use picture called LOSER that I have uploaded with image of man on left. Our logo should be on right side somewhere. Also, on the right side put text:

Big font heading that says:

"Don't be a LOSER"

Medium or smaller font text:

"Never lose a file again.
Just $75/year includes backup for
10 PCs or Macs with UNLIMITED SPACE
FREE 30-day TRIAL at www.ourAMBERstash.com”

Smaller font:
"BUSINESS USERS protect your Tallybooks, SCRIBE and other critical files.
HOME USERS protect your personal documents and family photos."

Some graphics to consider for side 1:
Small building to represent business, maybe an icon like one of these: https://www.pixoravista.example/find?q=office+building+icon&type=img&ref=qx81vT4mPz

Small house graphic to represent home users, maybe an icon like one of these
https://www.pixoravista.example/find?q=home+icon&type=img&ref=wd47kLn2Rb

With the text above layout the words as best as you can and use any additional graphics that you think would best generate interest in our service. Most likely showing computers and some file icons.

SIDE 2
We need to write address on right side of postcard. You can use left 1/2 or 2/3 for graphics and text below.

"Did you know:

A hard drive crashes every 15 seconds.
2,000 laptops are stolen or lost every day.
32% of data loss is caused by human error.
44% of data loss caused by hard drive failure.
100% of all computers eventually fail

JUST $75/YEAR
Includes up to 10 PCs or Macs with Unlimited Space.
FREE 30-day TRIAL at www.ourAMBERstash.com"

ourAMBERstash LOGO

Suggest you put a good graphic faded in the background of text.

Target Market(s)

Small businesses or home users

Industry/Entity Type

Building

Requirements
Must have
• Our logo - I have attached AI file.
Nice to have
• Communicate backup to our CLOUD SERVERS (as cloud is the latest catch phrase)

```html
<!DOCTYPE html>
<html lang="en">
<head>
<meta charset="utf-8">
<title>ourAMBERstash postcard</title>
<link rel="stylesheet" href="https://fonts.googleapis.com/css2?family=Anton&family=Roboto:wght@400;700;900&family=Open+Sans:wght@400;600&display=swap">
<style>
  :root{
    --page:#ffffff;
    --storm-dark:#0c0c0c;
    --storm-mid:#3a3a3a;
    --storm-light:#8a8a8a;
    --yellow:#ffef1a;
    --cream:#fbf6cf;
    --white:#ffffff;
    --green-dark:#0f5a12;
    --green:#1f8a1f;
    --green-bright:#35b035;
    --sticker:#fff45a;
    --sticker-edge:#e8dc2a;
    --skin:#b98a6e;
    --shirt:#e9e9e9;
  }
  *{box-sizing:border-box;margin:0;padding:0}
  html,body{width:1200px;height:600px;overflow:hidden;background:var(--page)}
  .postcard{position:absolute;left:32px;top:32px;width:1136px;height:536px;overflow:hidden;
    font-family:"Roboto",Arial,sans-serif;color:var(--white)}
  .storm-backdrop{position:absolute;inset:0;
    background:
      radial-gradient(circle at 92% 13%, var(--storm-light) 0, #555 9%, transparent 26%),
      radial-gradient(ellipse at 35% 75%, #4a4a4a 0, transparent 45%),
      radial-gradient(ellipse at 85% 70%, #5a5a5a 0, transparent 40%),
      linear-gradient(180deg, var(--storm-dark) 0%, #1b1b1b 45%, var(--storm-mid) 100%)}
  .portrait{position:absolute;left:0;top:170px;width:300px;height:366px;
    background:
      radial-gradient(ellipse at 45% 45%, var(--skin) 0, #8c6550 35%, transparent 62%),
      linear-gradient(180deg, transparent 60%, var(--shirt) 100%);
    opacity:.9}
  .headline{position:absolute;left:60px;top:52px;width:270px;text-align:center;
    font-family:"Anton",Impact,sans-serif;line-height:1;text-shadow:0 3px 6px rgba(0,0,0,.7)}
  .headline .lead{display:block;font-size:62px;color:var(--cream);letter-spacing:.5px}
  .headline .loser{display:block;font-size:80px;color:var(--yellow);margin-top:4px;letter-spacing:1px}
  .divider{position:absolute;left:343px;top:52px;width:2px;height:146px;background:var(--white)}
  .offer{position:absolute;left:377px;top:52px}
  .offer h2{font-weight:900;font-size:29px;letter-spacing:.3px}
  .offer h2 em{font-style:normal;color:var(--yellow)}
  .offer ul{list-style:none;margin-top:14px}
  .offer li{position:relative;padding-left:22px;font-size:21px;line-height:1.2;margin-bottom:14px}
  .offer li::before{content:"";position:absolute;left:2px;top:9px;width:8px;height:8px;border-radius:50%;background:var(--green-bright)}
  .offer strong{font-weight:900}
  .hi{color:var(--yellow);font-weight:900}
  .hi-line{color:var(--yellow);font-weight:900;border-bottom:2px solid var(--yellow)}
  .os-marks{display:inline-flex;gap:10px;vertical-align:middle;margin-left:22px}
  .os-marks span{width:30px;height:30px;background:#d8d8d8;border-radius:4px}
  .user-panel{position:absolute;left:340px;top:220px;width:520px;height:294px;border-radius:10px;
    background:linear-gradient(180deg,var(--green) 0%,var(--green-dark) 100%)}
  .segment{position:absolute;left:0;width:100%}
  .segment.business{top:20px}
  .segment.home{top:166px}
  .segment .glyph{position:absolute;left:22px;top:0;width:52px;height:68px;border-radius:4px;
    background:linear-gradient(135deg,#e6eef2,#9fb0b8)}
  .segment.home .glyph{height:56px;background:linear-gradient(135deg,#f4f4f4,#a9b4a0)}
  .segment h3{position:absolute;left:105px;top:10px;font-weight:900;font-size:19px;color:var(--yellow);letter-spacing:.3px}
  .segment p{position:absolute;left:105px;top:34px;font-size:14px;font-weight:700;white-space:nowrap}
  .file-row{position:absolute;left:107px;top:73px;display:flex;gap:15px}
  .segment.home .file-row{top:73px}
  .file-row span{width:42px;height:44px;border-radius:6px;background:linear-gradient(180deg,#fafafa,#cfcfcf);
    box-shadow:0 2px 3px rgba(0,0,0,.4)}
  .file-row.round span:first-child,.file-row.round span:last-child{border-radius:50%}
  .panel-rule{position:absolute;left:105px;right:20px;top:157px;height:1px;background:rgba(255,255,255,.25)}
  .trial-sticker{position:absolute;left:828px;top:243px;width:178px;height:177px;border-radius:14px;
    background:linear-gradient(180deg,var(--sticker) 0%,var(--sticker-edge) 100%);
    box-shadow:0 4px 10px rgba(0,0,0,.5);text-align:center;color:var(--green-dark)}
  .trial-sticker svg{position:absolute;right:0;top:0}
  .trial-sticker .free{display:block;font-family:"Anton",Impact,sans-serif;font-size:56px;line-height:1;margin-top:18px;color:var(--green)}
  .trial-sticker .days{display:block;margin:8px 6px 0;padding:4px 0;font-weight:900;font-size:19px;color:#555;
    background:linear-gradient(180deg,#fff9a8,var(--sticker-edge))}
  .trial-sticker .at{display:block;font-weight:700;font-size:13px;margin-top:8px}
  .trial-sticker .url{display:block;font-weight:700;font-size:12px;margin-top:2px}
  .brand{position:absolute;left:906px;top:452px;display:flex;align-items:center;gap:8px}
  .brand .mark{width:24px;height:24px;background:var(--green-bright)}
  .brand .name{font-family:"Roboto",Arial,sans-serif;font-weight:700;font-size:20px;color:var(--white)}
  .brand-note{position:absolute;left:906px;top:484px;font-family:"Open Sans",Arial,sans-serif;font-size:9px;color:var(--white)}
</style>
</head>
<body>
<main class="postcard">
  <div class="storm-backdrop" role="img" aria-label="Dark stormy sky with lightning and a hurricane swirl at upper right"></div>
  <div class="portrait" role="img" aria-label="Photo of a bearded man in glasses and bow tie making an L sign on his forehead"></div>

  <h1 class="headline"><span class="lead">Don't be a</span><span class="loser">LOSER</span></h1>
  <div class="divider"></div>

  <section class="offer">
    <h2>NEVER <em>LOSE</em> A FILE AGAIN</h2>
    <ul>
      <li><strong class="hi">Just <span style="color:var(--yellow)">$75/year</span></strong> for online backup for<br>up to 10 computers with <span class="hi-line">UNLIMITED SPACE</span></li>
      <li>Available for <span class="hi">Paneview &amp; Orchard</span><span class="os-marks"><span></span><span></span></span></li>
    </ul>
  </section>

  <section class="user-panel">
    <div class="segment business">
      <div class="glyph" role="img" aria-label="Office building icon"></div>
      <h3>BUSINESS USERS</h3>
      <p>protect your Tallybooks, SCRIBE and other files.</p>
      <div class="file-row"><span></span><span></span><span></span><span></span><span></span></div>
    </div>
    <div class="panel-rule"></div>
    <div class="segment home">
      <div class="glyph" role="img" aria-label="House icon"></div>
      <h3>HOME USERS</h3>
      <p>protect your personal files including family photos.</p>
      <div class="file-row round"><span></span><span></span><span></span><span></span><span></span></div>
    </div>
  </section>

  <aside class="trial-sticker">
    <svg width="30" height="30" viewBox="0 0 30 30" aria-hidden="true">
      <path d="M0 0 L30 30 L0 30 Z" fill="#fffbd0"/>
      <path d="M0 0 L30 0 L30 30 Z" fill="#2a2a2a"/>
    </svg>
    <span class="free">FREE</span>
    <span class="days">30 DAY TRIAL</span>
    <span class="at">at</span>
    <span class="url">www.ourAMBERstash.com</span>
  </aside>

  <div class="brand"><span class="mark"></span><span class="name">ourAMBERstash</span></div>
  <div class="brand-note">A service from Parcelline Corporation</div>
</main>
</body>
</html>
```